Zielgruppe
Verkauf von Spielwaren
Zielgruppe sind Kinder und ihre Eltern
Aufgabenstellung
-Logo sollte wenn möglich integriert werden, da seit 25 Jahren bekannt
-Breite 220cm, Höhe 210cm (nimmt ein komplettes Schaufenster ein)
-www.spielkiste-mauerbach.de
Aktuell sieht man von dieser Seite des Gebäudes nicht, dass es sich um ein Spielwarengeschäft handelt. Das Plakat soll potentielle Kunden darauf aufmerksam machen, daher auffällig und eindeutig spielwarenbezogen sein. Desweiteren sind wir ein Familienunternehmen mit breiter Produktpalette und das Plakat soll ganzjährig genutzt werden und demzufolge saisonunabhängig gestaltet sein.

```html
<!DOCTYPE html>
<html lang="de">
<head>
<meta charset="utf-8">
<title>Spielkiste – Schaufensterplakat</title>
<link rel="stylesheet" href="https://fonts.googleapis.com/css2?family=Fredoka:wght@500;600;700&display=swap">
<style>
  :root {
    --page-bg: #ececec;
    --poster-bg: #ffffff;
    --brand-red: #d7141e;
    --band-red: #cc0f17;
    --arrow-yellow: #f7c415;
    --text-white: #ffffff;
    --shadow: rgba(0,0,0,0.12);
  }
  * { margin: 0; padding: 0; box-sizing: border-box; }
  html, body {
    width: 1200px;
    height: 848px;
    overflow: hidden;
    background: var(--page-bg);
    font-family: "Fredoka", "Arial Rounded MT Bold", sans-serif;
  }
  .poster {
    position: absolute;
    left: 192px;
    top: 34px;
    width: 816px;
    height: 780px;
    background: var(--poster-bg);
    box-shadow: 0 4px 18px var(--shadow);
    overflow: hidden;
  }
  .brand-band {
    position: absolute;
    left: 0; top: 0;
    width: 100%;
    height: 64px;
    background: var(--band-red);
    color: var(--text-white);
    font-weight: 600;
    font-size: 23px;
    letter-spacing: 0.3px;
    display: flex;
    align-items: center;
    justify-content: center;
    white-space: nowrap;
  }
  .illustration {
    position: absolute;
    border-radius: 24px;
  }
  .illustration--kid-castle {
    left: 12px;
    top: 90px;
    width: 390px;
    height: 676px;
    background: linear-gradient(180deg, #d9574a 0%, #f2c9a8 22%, #4a78c2 45%, #e9c27a 70%, #c8a24f 100%);
  }
  .illustration--robot {
    left: 410px;
    top: 500px;
    width: 140px;
    height: 220px;
    background: linear-gradient(180deg, #f0a33a 0%, #e26a2c 55%, #c9452a 100%);
  }
  .shop-name {
    position: absolute;
    left: 390px;
    top: 130px;
    display: flex;
    align-items: center;
    gap: 16px;
  }
  .shop-name__square {
    width: 46px;
    height: 46px;
    background: var(--brand-red);
    border-radius: 6px;
  }
  .shop-name__text {
    font-weight: 700;
    font-size: 58px;
    color: var(--brand-red);
    line-height: 1;
  }
  .slogan {
    position: absolute;
    left: 415px;
    top: 270px;
    width: 360px;
    color: var(--brand-red);
    font-weight: 700;
    font-size: 52px;
    line-height: 62px;
    letter-spacing: 1px;
  }
  .slogan span { display: block; }
  .slogan .indent { padding-left: 8px; }
  .entrance-arrow {
    position: absolute;
    left: 560px;
    top: 470px;
    width: 230px;
    height: 130px;
  }
  .entrance-arrow__label {
    position: absolute;
    left: 568px;
    top: 512px;
    width: 170px;
    text-align: center;
    color: var(--text-white);
    font-weight: 600;
    font-size: 38px;
    line-height: 44px;
  }
</style>
</head>
<body>
  <main class="poster">
    <header class="brand-band">Steinwerk • Figurino • weitere Marken bzw. Spielsachen • usw</header>

    <div class="illustration illustration--kid-castle" role="img" aria-label="Illustration: winkender Junge mit roten Locken in Latzhose, dahinter eine Spielzeugburg und ein Springteufel-Clown"></div>
    <div class="illustration illustration--robot" role="img" aria-label="Illustration: orangefarbener Spielzeugroboter"></div>

    <div class="shop-name">
      <span class="shop-name__square"></span>
      <span class="shop-name__text">Spielkiste</span>
    </div>

    <p class="slogan">
      <span>„Hier ist</span>
      <span>der Spaß</span>
      <span class="indent">zuhause!“</span>
    </p>

    <svg class="entrance-arrow" viewBox="0 0 230 130" aria-hidden="true">
      <path d="M0 34 H150 V0 L230 65 L150 130 V96 H0 Z" fill="var(--arrow-yellow)" rx="10"/>
    </svg>
    <div class="entrance-arrow__label">Eingang</div>
  </main>
</body>
</html>
```